A Serene Bay Spa Hotel needs Creative VIP Cards Design

We need VIP Cards Design for a SPA Plaza Hotel, This Serene Bay Spa Hotel have multiple sub projects, such as leisure hotel room, large buffet restaurant, swimming pool, theatrical performances, sauna bath, massage, SPA, Tea bar, 3D cinema, KTV rooms, chess room, Internet cafes , art appreciation, children's Castle, Korean geothermal, table tennis, billiard room, GYM and other entertainments.
We need Three creative VIP Card design for 3 different level:
1. Golden Card
2. Platinum Card
3. Diamond Card
Attached, Please find the LOGO file and some sample, we new design with much better look than those samples.

```html
<!DOCTYPE html>
<html lang="en">
<head>
<meta charset="utf-8">
<title>VIP Gold Membership Card</title>
<link href="https://fonts.googleapis.com/css2?family=Cinzel:wght@600;700&family=Noto+Sans+TC:wght@400;500&family=Noto+Serif+TC:wght@700&family=Open+Sans:wght@400;600&family=Pinyon+Script&family=Roboto+Condensed:wght@500&display=swap" rel="stylesheet">
<style>
  :root {
    --page-light: #fbfbfb;
    --page-shade: #d9d9d9;
    --label-ink: #333333;
    --card-black: #050505;
    --card-text: #ffffff;
    --panel-white: #f4f4f4;
    --brand-cyan: #3fd0ea;
    --brand-amber: #d99a12;
    --gold-light: #fff3b0;
    --gold-mid: #e8b631;
    --gold-deep: #8a5a08;
    --gold-flat: #f2c53d;
    --gold-grad: linear-gradient(180deg, var(--gold-light) 0%, var(--gold-mid) 45%, var(--gold-deep) 62%, var(--gold-mid) 80%, var(--gold-light) 100%);
  }
  * { margin: 0; padding: 0; box-sizing: border-box; }
  html, body { width: 1200px; height: 1198px; overflow: hidden; }
  body {
    position: relative;
    background: radial-gradient(ellipse at 55% 40%, var(--page-light) 0%, #eeeeee 60%, var(--page-shade) 100%);
    font-family: "Open Sans", sans-serif;
  }
  .stage-label {
    position: absolute; left: 70px; top: 86px;
    font-family: "Roboto Condensed", sans-serif; font-weight: 500;
    font-size: 94px; line-height: 82px; color: var(--label-ink);
    text-align: center; letter-spacing: 1px;
  }
  .card {
    position: absolute; background: var(--card-black);
    border-radius: 12px; overflow: hidden; color: var(--card-text);
  }
  .gold-text {
    background: var(--gold-grad);
    -webkit-background-clip: text; background-clip: text;
    color: transparent;
    padding-right: 0.25em;
  }

  /* back of card */
  .card-back { left: 480px; top: 102px; width: 654px; height: 414px; }
  .card-back .hotel-name {
    position: absolute; right: 24px; top: 24px;
    font-weight: 600; font-size: 21px; letter-spacing: .5px;
  }
  .card-back .signature-label-zh {
    position: absolute; left: 19px; top: 52px;
    font-family: "Noto Sans TC", sans-serif; font-size: 21px; letter-spacing: 2px;
  }
  .card-back .signature-label-en {
    position: absolute; left: 18px; top: 86px; font-size: 20px;
  }
  .card-back .signature-panel {
    position: absolute; left: 17px; top: 121px; width: 476px; height: 55px;
    background: var(--panel-white);
  }
  .card-back .terms {
    position: absolute; left: 18px; top: 193px; font-size: 16px; line-height: 21px;
  }
  .card-back .terms p { margin-bottom: 9px; }
  .card-back .terms .zh { font-family: "Noto Sans TC", sans-serif; display: block; letter-spacing: 1px; }
  .card-back .card-number {
    position: absolute; left: 114px; top: 363px;
    font-family: "Noto Sans TC", sans-serif; font-size: 19px; letter-spacing: 1.5px;
  }
  .card-back .tier-mark { position: absolute; left: 432px; top: 318px; width: 222px; height: 90px; }
  .tier-mark .tier-vip {
    position: absolute; left: 0; top: 2px;
    font-family: "Cinzel", serif; font-weight: 700; font-size: 48px;
  }
  .tier-mark .tier-word {
    position: absolute; left: 94px; top: 4px;
    font-family: "Pinyon Script", cursive; font-size: 54px; line-height: 70px;
  }
  .tier-mark .tier-zh {
    position: absolute; left: 128px; top: 62px;
    font-family: "Noto Serif TC", serif; font-weight: 700; font-size: 17px; color: var(--gold-flat);
  }

  /* front of card */
  .card-front { left: 220px; top: 588px; width: 849px; height: 540px; }
  .card-front .swooshes { position: absolute; inset: 0; }
  .card-front .ornament {
    position: absolute; left: 0; top: 0; width: 170px; height: 170px;
    background: radial-gradient(circle at 30% 30%, #e6b83a 0%, #a9780f 45%, rgba(5,5,5,0) 75%);
  }
  .brand {
    position: absolute; left: 110px; top: 62px; width: 280px; text-align: center;
    color: var(--brand-cyan); font-family: "Noto Sans TC", sans-serif; font-weight: 500;
  }
  .brand .brand-dot {
    width: 58px; height: 58px; border-radius: 50%; background: var(--brand-amber);
    margin: 0 auto 14px;
  }
  .brand .brand-zh { font-size: 32px; line-height: 38px; letter-spacing: 2px; }
  .brand .brand-en { font-size: 19px; line-height: 26px; }
  .card-front .vip {
    position: absolute; left: 420px; top: 46px;
    font-family: "Cinzel", serif; font-weight: 700; font-size: 196px; line-height: 200px;
  }
  .card-front .tier-word {
    position: absolute; left: 72px; top: 246px;
    font-family: "Pinyon Script", cursive; font-size: 205px; line-height: 240px;
  }
  .card-front .tier-zh {
    position: absolute; left: 206px; top: 438px;
    font-family: "Noto Serif TC", serif; font-weight: 700; font-size: 40px; color: var(--gold-flat);
  }
  .card-front .card-number {
    position: absolute; left: 537px; top: 468px;
    font-family: "Cinzel", serif; font-weight: 600; font-size: 32px; color: var(--gold-flat);
  }
</style>
</head>
<body>
  <div class="stage-label">INITIAL<br>DESIGN</div>

  <section class="card card-back">
    <div class="hotel-name">SERENE BAY SPA HOTEL</div>
    <div class="signature-label-zh">授權簽名</div>
    <div class="signature-label-en">AUTHORIZED SIGNATURE</div>
    <div class="signature-panel"></div>
    <div class="terms">
      <p>Please show your membership card when you check out.<span class="zh">請出示您的會員卡，當你退房。</span></p>
      <p>Signature and use of this card confirms the acceptance of the<span class="zh">簽名和使用此卡的確認驗收</span></p>
      <p>Term and Conditions of Membership.<span class="zh">期限和會員的條件。</span></p>
    </div>
    <div class="card-number">這裡樣本數 ：123 4567 890</div>
    <div class="tier-mark">
      <span class="tier-vip gold-text">VIP</span>
      <span class="tier-word gold-text">Gold</span>
      <span class="tier-zh">黃金</span>
    </div>
  </section>

  <section class="card card-front">
    <svg class="swooshes" width="849" height="540" viewBox="0 0 849 540">
      <defs>
        <linearGradient id="gold-band" x1="0" y1="0" x2="1" y2="1">
          <stop offset="0" stop-color="#fff0a0"/>
          <stop offset=".5" stop-color="#d9a222"/>
          <stop offset="1" stop-color="#fbe27a"/>
        </linearGradient>
      </defs>
      <path d="M0,128 Q110,40 280,0 L318,0 Q130,55 0,160 Z" fill="url(#gold-band)"/>
      <path d="M0,172 Q150,60 350,0 L356,0 Q150,66 0,178 Z" fill="url(#gold-band)"/>
      <path d="M250,540 Q560,440 849,150 L849,205 Q600,470 340,540 Z" fill="url(#gold-band)"/>
      <path d="M380,540 Q630,460 849,235 L849,242 Q640,468 396,540 Z" fill="url(#gold-band)"/>
    </svg>
    <div class="ornament" role="img" aria-label="Gold baroque flourish ornament in the corner"></div>
    <div class="brand">
      <div class="brand-dot"></div>
      <div class="brand-zh">静湾休闲广场</div>
      <div class="brand-en">Serene Bay Leisure Plaza</div>
    </div>
    <div class="vip gold-text">VIP</div>
    <div class="tier-word gold-text">Gold</div>
    <div class="tier-zh">黃金</div>
    <div class="card-number">NO. 123 4567 890</div>
  </section>
</body>
</html>
```